Clear Plastic Card Design

I am looking to have a business card designed from my logo icon. I am looking to match the style of a different business card I have attached in the files.
Looking for a card that is plastic, with layers of transparency in the shape of my logo icon (also attached in the files) - not a circle like the other card. The winning design will incorporate the red icon logo on the front and back and include the charity's name, "Lanterns of Willow Creek" in the same or similar font, as well as an email and phone number. For now, use the email: email@lanternsofwillowcreek.org and the phone number 555-014-7392.
We like how the sample business card has transparency, partial and full opacity layers and a matching color scheme. Files will need to be in vector so that our business card printing company can work with it.
UPDATE:
We've some excellent designs in, thank you everyone! I got an early review from the owner, and he requested a minor redirect to find his perfect design. He wants the design to stand out by NOT being a rectangle. Try instead a circle, square, or best yet - something that falls in the outline of the logo icon, either fully or partially. Thank you, everyone!
Lanterns of Willow Creek text should be incorporated as well as a phone and email.

```html
<!DOCTYPE html>
<html lang="en">
<head>
<meta charset="utf-8">
<title>Lanterns of Willow Creek — Business Card</title>
<link rel="stylesheet" href="https://fonts.googleapis.com/css2?family=Outfit:wght@300&family=Open+Sans:wght@400;600&display=swap">
<style>
  :root {
    --page-bg: #e9e4dc;
    --card-black: #000000;
    --card-clear-top: #efe7dc;
    --card-clear-bottom: #d9cfc2;
    --title-cream: #f1e9dc;
    --name-orange: #d9561f;
    --role-tan: #b9a68c;
    --contact-tan: #a38b6b;
    --icon-orange: #c8461c;
    --brand-red: #c41f18;
    --brand-frame: #e8ddd0;
    --card-edge: #f3e6c6;
  }
  * { margin: 0; padding: 0; box-sizing: border-box; }
  html, body {
    width: 1200px;
    height: 926px;
    overflow: hidden;
    background: var(--page-bg);
  }
  .canvas {
    position: relative;
    width: 1200px;
    height: 926px;
  }
  .card {
    position: absolute;
    left: 50px;
    top: 155px;
    width: 1100px;
    height: 615px;
    border: 1px solid var(--card-edge);
    background: linear-gradient(160deg, var(--card-clear-top), var(--card-clear-bottom));
    overflow: hidden;
    box-shadow: 0 10px 30px rgba(0,0,0,0.15);
  }
  .card__dark-panel {
    position: absolute;
    left: 0;
    top: 0;
    width: 676px;
    height: 100%;
    background: var(--card-black);
  }
  .card__title {
    position: absolute;
    left: 44px;
    top: 56px;
    font-family: "Outfit", sans-serif;
    font-weight: 300;
    font-size: 52px;
    line-height: 64px;
    color: var(--title-cream);
    letter-spacing: 0.3px;
    white-space: nowrap;
  }
  .card__person {
    position: absolute;
    left: 50px;
    top: 380px;
    font-family: "Open Sans", sans-serif;
  }
  .card__name {
    font-weight: 600;
    font-size: 38px;
    line-height: 44px;
    color: var(--name-orange);
    letter-spacing: 0.5px;
  }
  .card__role {
    font-weight: 400;
    font-size: 28px;
    line-height: 36px;
    color: var(--role-tan);
  }
  .card__contacts {
    position: absolute;
    left: 48px;
    top: 486px;
    font-family: "Open Sans", sans-serif;
    font-size: 28px;
    color: var(--contact-tan);
    list-style: none;
  }
  .card__contact {
    display: flex;
    align-items: center;
    gap: 10px;
    height: 39px;
    white-space: nowrap;
  }
  .card__contact svg { width: 22px; height: 22px; flex: none; }
  .card__brand-square {
    position: absolute;
    left: 470px;
    top: 56px;
    width: 320px;
    height: 320px;
    background: var(--brand-red);
    border: 14px solid var(--brand-frame);
    border-radius: 10px;
  }
  .card__brand-name {
    position: absolute;
    left: 812px;
    top: 392px;
    font-family: "Open Sans", sans-serif;
    font-weight: 600;
    font-size: 32px;
    line-height: 40px;
    color: var(--brand-red);
  }
</style>
</head>
<body>
  <main class="canvas">
    <section class="card" aria-label="Business card">
      <div class="card__dark-panel"></div>

      <div class="card__brand-square" aria-hidden="true"></div>
      <p class="card__brand-name">Lanterns of<br>Willow Creek</p>

      <h1 class="card__title">Lanterns of<br>Willow Creek</h1>

      <div class="card__person">
        <p class="card__name">DANIEL REYES</p>
        <p class="card__role">Managing Director</p>
      </div>

      <ul class="card__contacts">
        <li class="card__contact">
          <svg viewBox="0 0 24 24" aria-hidden="true">
            <path fill="var(--icon-orange)" d="M3 9c0-3 4-5 9-5s9 2 9 5v2h-5V9c-1-.6-2.5-1-4-1s-3 .4-4 1v2H3z M6 12h12l2 8H4z M12 14a2.5 2.5 0 1 0 0 5a2.5 2.5 0 1 0 0-5z"/>
          </svg>
          <span>555-014-7392</span>
        </li>
        <li class="card__contact">
          <svg viewBox="0 0 24 24" aria-hidden="true">
            <path fill="var(--icon-orange)" d="M2 9l10-6 10 6v12H2z"/>
            <path fill="none" stroke="#000" stroke-width="1.5" d="M2 9l10 7 10-7M2 21l7-7M22 21l-7-7"/>
          </svg>
          <span>email@lanternsofwillowcreek.org</span>
        </li>
      </ul>
    </section>
  </main>
</body>
</html>
```